velto renovation roof

We need a flyer for a new york based company called velto renovations. We are looking to promote our roofing/window/siding/concrete service.

We are a construction company with over 30 years in the business, but have set up a new company to specialize in roofing - windows - siding. We do offer general renovation service both interior (tiles, paint , Sheetrock, etc) as well as concrete work (driveways, sidewalk) but we think it may be to much information for the flyer. We are fully insured and licensed

We are open to all ideas (I will include a picture of a design that caught our eye from your site).

Target Market(s)

home owners, building managers in the tri state area. We are a New York based company

Industry/Entity Type

Construction

```html
<!DOCTYPE html>
<html lang="en">
<head>
<meta charset="utf-8">
<title>Velto Renovations – Flyer</title>
<link rel="stylesheet" href="https://fonts.googleapis.com/css2?family=Open+Sans:wght@400;600;700;800&display=swap">
<style>
  :root {
    --bg-dark: #262626;
    --bg-dark-2: #333333;
    --plank-light: #d9d9d9;
    --plank-light-2: #bfbfbf;
    --accent-blue: #1fa9e1;
    --accent-yellow: #f2e600;
    --white: #ffffff;
    --black: #111111;
  }
  * { box-sizing: border-box; margin: 0; padding: 0; }
  html, body {
    width: 1200px; height: 566px; overflow: hidden;
    background: var(--bg-dark);
  }
  .flyer {
    position: relative; width: 1200px; height: 566px; overflow: hidden;
    font-family: "Open Sans", Arial, sans-serif;
    color: var(--white);
    background: linear-gradient(180deg, var(--bg-dark-2) 0%, var(--bg-dark) 45%, #1c1c1c 100%);
  }
  .brand-name {
    position: absolute; left: 48px; top: 50px;
    font-size: 92px; font-weight: 600; letter-spacing: -1px; line-height: 1;
    color: var(--white);
  }
  .brand-mark {
    position: absolute; left: 1040px; top: 92px;
    width: 44px; height: 44px; background: var(--accent-blue);
  }
  .service-band {
    position: absolute; left: 0; top: 190px; width: 1200px; height: 60px;
    background: var(--accent-blue);
    display: flex; align-items: center; padding-left: 34px;
  }
  .service {
    display: flex; align-items: center;
    font-size: 32px; font-weight: 700; color: var(--white);
    margin-right: 50px; line-height: 1;
  }
  .service svg { margin-right: 14px; }
  .gallery-band {
    position: absolute; left: 0; top: 262px; width: 1200px; height: 196px;
    background: linear-gradient(180deg, var(--plank-light) 0%, var(--plank-light-2) 100%);
  }
  .gallery {
    position: absolute; top: 272px; left: 0; width: 1200px; height: 176px;
  }
  .photo {
    position: absolute; top: 0; height: 176px;
    border: 9px solid var(--black);
  }
  .photo--roofing { left: 12px; width: 254px;
    background: linear-gradient(160deg, #e6e1d6 0%, #b9a28a 35%, #c23a38 70%, #8e2a2a 100%); }
  .photo--window { left: 276px; width: 228px;
    background: linear-gradient(90deg, #cfd3d6 0%, #f1f1f1 45%, #a9a39a 100%); }
  .photo--siding { left: 514px; width: 232px;
    background: linear-gradient(120deg, #f0e9dc 0%, #dcc9a6 45%, #b8392f 70%, #d8c7a2 100%); }
  .photo--concrete { left: 756px; width: 232px;
    background: linear-gradient(135deg, #cfc9bf 0%, #a9a398 55%, #8a857c 100%); }
  .experience-badge {
    position: absolute; left: 998px; top: 262px; width: 202px; height: 196px;
    background: var(--black);
  }
  .experience-over {
    position: absolute; left: 20px; top: 130px;
    font-size: 34px; font-weight: 700; line-height: 1; color: var(--white);
    transform: rotate(-90deg); transform-origin: left top;
    white-space: nowrap;
  }
  .experience-number {
    position: absolute; left: 58px; top: 34px;
    font-size: 100px; font-weight: 700; line-height: 1; letter-spacing: -3px;
    color: var(--accent-blue);
  }
  .experience-label {
    position: absolute; left: 22px; top: 146px;
    font-size: 15px; font-weight: 700; line-height: 1; color: var(--white);
    white-space: nowrap;
  }
  .call-to-action {
    position: absolute; left: 46px; top: 466px;
    display: flex; align-items: baseline; gap: 22px;
    color: var(--accent-yellow); font-weight: 700; line-height: 1;
    white-space: nowrap;
  }
  .call-to-action__lead { font-size: 30px; }
  .call-to-action__phone-label { font-size: 36px; }
  .call-to-action__phone { font-size: 54px; font-weight: 600; letter-spacing: 1px; margin-left: -8px; }
  .contact-line {
    position: absolute; left: 46px; top: 526px;
    font-size: 21px; font-weight: 400; line-height: 1; color: var(--white);
    white-space: nowrap;
  }
</style>
</head>
<body>
<main class="flyer">
  <h1 class="brand-name">Velto Renovations</h1>
  <span class="brand-mark" aria-hidden="true"></span>

  <nav class="service-band" aria-label="Services">
    <span class="service"><svg width="12" height="18" viewBox="0 0 12 18"><polygon points="0,0 12,9 0,18" fill="#fff"/></svg>Roofing</span>
    <span class="service"><svg width="12" height="18" viewBox="0 0 12 18"><polygon points="0,0 12,9 0,18" fill="#fff"/></svg>Window</span>
    <span class="service"><svg width="12" height="18" viewBox="0 0 12 18"><polygon points="0,0 12,9 0,18" fill="#fff"/></svg>Siding</span>
    <span class="service"><svg width="12" height="18" viewBox="0 0 12 18"><polygon points="0,0 12,9 0,18" fill="#fff"/></svg>Concrete service</span>
  </nav>

  <div class="gallery-band" aria-hidden="true"></div>
  <section class="gallery" aria-label="Service photos">
    <div class="photo photo--roofing" role="img" aria-label="Roofers laying red roof tiles"></div>
    <div class="photo photo--window" role="img" aria-label="Installer fitting a window frame with a drill"></div>
    <div class="photo photo--siding" role="img" aria-label="Worker installing beige house siding"></div>
    <div class="photo photo--concrete" role="img" aria-label="Hand smoothing fresh concrete with a trowel"></div>
  </section>

  <aside class="experience-badge">
    <span class="experience-over">Over</span>
    <span class="experience-number">30</span>
    <span class="experience-label">Years of Experience!</span>
  </aside>

  <p class="call-to-action">
    <span class="call-to-action__lead">Start your Renovations TODAY!</span>
    <span class="call-to-action__phone-label">Call:</span>
    <span class="call-to-action__phone">555 214 7380</span>
  </p>

  <p class="contact-line">125 Harbor Street, Brooklyn, NY | &nbsp;www.veltorenovations.com | e-mail: veltorenovations@mail.com</p>
</main>
</body>
</html>
```